Norvale Email Signature Banners – Fabrication Capability Series

www.Norvale.com.au is an Australian engineering and fabrication company specialising in fabrication and welding of :
steel piping spools,
skids and frames,
small volume process steel tanks
and general steel fabrication
We require four distinct banner designs for use in Teldrin Quillmark email signatures. Each banner will highlight a specific capability while maintaining a consistent brand identity.
Deliverables
Four banners total:
Piping Spools Fabrication – focus on precision welding and stainless steel pipework
Skid & Frames Fabrication – highlight skid systems and structural frames
Small Steel Tanks Fabrication – show fabricated tanks and workshop craftsmanship
General Fabrication Solutions – broad steel fabrication theme for company-wide use
Dimensions: 600–700 px wide × 100 px high
Format: PNG (preferred), small file size prefered
Resolution: 72 dpi
Background: non-transparent, industrial or workshop setting
Text examples:
1. Piping Spools Fabrication
Option A: “Expert Fabrication Solutions for Process Piping”
Option B: “Precision Welding for Complex Systems”
Option C: “Delivering Quality in Every Spool”
Option D: “Engineered for Flow, Built for Strength”
2. Skid & Frames Fabrication
Option A: “Custom Engineered Modular Systems”
Option B: “Built Strong. Designed Smart.”
Option C: “Reliable Frames for Industrial Performance”
Option D: “Modular Fabrication for Seamless Integration”
3. Small Steel Tanks Fabrication
Option A: “Precision Built for Your Needs”
Option B: “Compact Strength. Proven Durability.”
Option C: “Fabricated for Performance and Longevity”
Option D: “Small Tanks. Big Reliability.”
4. General Fabrication Solutions
Option A: “Quality Craftsmanship, Proven Results”
Option B: “Your Partner in Precision Fabrication”
Option C: “Engineering Excellence in Every Weld”
Option D: “Australian Fabrication. Global Standards.”
Style Direction
Clean, professional, and engineering‑focused
Use Norvale brand colours
Blend photo realism with vector clarity (no heavy gradients)
Include subtle industrial textures or workshop imagery
Typography: bold sans‑serif, legible at small scale
Usage Context
These banners will appear at the bottom of staff email signatures via Quillmark Email Signature Tool for Teldrin 365, so clarity and fast loading are essential. No Logo is required in the banners.
Reference
Existing Norvale signature is attached. Colour palette to match the signature style and logo.
Target Market(s)
Engineering and construction companies,
Industry/Entity Type
Engineering fabrication design

```html
<!DOCTYPE html>
<html lang="en">
<head>
<meta charset="utf-8">
<title>Norvale Email Signature Banners – Fabrication Capability Series</title>
<link rel="stylesheet" href="https://fonts.googleapis.com/css2?family=Poppins:ital,wght@1,800&family=Roboto:wght@700&display=swap">
<style>
  :root {
    --stage: #657279;
    --brand-blue: #22a7e0;
    --steel-grey: #939598;
    --paper: #ffffff;
    --ink: #3a3a3a;
  }
  html, body {
    margin: 0;
    padding: 0;
    width: 1200px;
    height: 938px;
    overflow: hidden;
    background: var(--stage);
  }
  .banner-set {
    position: relative;
    width: 1200px;
    height: 938px;
  }
  .banner {
    position: absolute;
    left: 150px;
    width: 878px;
    height: 146px;
    display: block;
    filter: drop-shadow(0 8px 8px rgba(0, 0, 0, 0.28));
  }
  .banner--spools  { top: 84px; }
  .banner--skids   { top: 290px; }
  .banner--tanks   { top: 497px; }
  .banner--general { top: 703px; }

  .fill-paper { fill: var(--paper); }
  .fill-blue  { fill: var(--brand-blue); }
  .fill-grey  { fill: var(--steel-grey); }

  .headline {
    font-family: "Poppins", "Arial Black", sans-serif;
    font-style: italic;
    font-weight: 800;
    fill: var(--paper);
  }
  .tagline {
    font-family: "Roboto", Arial, sans-serif;
    font-weight: 700;
  }
  .tagline--dark  { fill: var(--ink); }
  .tagline--light { fill: var(--paper); }
  .brand-name {
    font-family: "Roboto", Arial, sans-serif;
    font-weight: 700;
    fill: var(--brand-blue);
    letter-spacing: 3px;
  }
</style>
</head>
<body>
<main class="banner-set">

  <!-- Piping spools -->
  <svg class="banner banner--spools" viewBox="0 0 1464 244" role="img" aria-label="Piping Spools Fabrication banner">
    <rect class="fill-paper" width="1464" height="244"/>
    <polygon class="fill-blue" points="355,0 1110,0 1060,244 290,244"/>
    <polygon class="fill-blue" points="1123,0 1142,0 1093,244 1074,244"/>
    <polygon class="fill-grey" points="1155,0 1190,0 1153,180 1118,180"/>
    <text class="brand-name" x="155" y="140" font-size="50" text-anchor="middle">NORVALE</text>
    <text class="headline" x="370" y="118" font-size="92" textLength="700" lengthAdjust="spacingAndGlyphs">PIPING SPOOLS</text>
    <text class="headline" x="418" y="205" font-size="92" textLength="604" lengthAdjust="spacingAndGlyphs">FABRICATION</text>
    <g class="tagline tagline--dark" font-size="36">
      <text x="1198" y="58">Focus on</text>
      <text x="1198" y="96">precision</text>
      <text x="1198" y="133">welding and</text>
      <text x="1198" y="171">stainless steel</text>
      <text x="1198" y="208">pipework</text>
    </g>
  </svg>

  <!-- Skids and frames -->
  <svg class="banner banner--skids" viewBox="0 0 1464 244" role="img" aria-label="Skid and Frames Fabrication banner">
    <rect class="fill-paper" width="1464" height="244"/>
    <polygon class="fill-blue" points="0,0 775,0 715,244 0,244"/>
    <polygon class="fill-blue" points="787,0 810,0 750,244 727,244"/>
    <polygon class="fill-grey" points="823,0 840,0 800,162 783,162"/>
    <text class="headline" x="30" y="116" font-size="92" textLength="685" lengthAdjust="spacingAndGlyphs">SKID &amp; FRAMES</text>
    <text class="headline" x="85" y="204" font-size="92" textLength="597" lengthAdjust="spacingAndGlyphs">FABRICATION</text>
    <g class="tagline tagline--dark" font-size="42">
      <text x="857" y="64">Highlight</text>
      <text x="857" y="116">skid systems</text>
      <text x="857" y="168">and structural</text>
      <text x="857" y="219">frames</text>
    </g>
    <text class="brand-name" x="1277" y="140" font-size="50" text-anchor="middle">NORVALE</text>
  </svg>

  <!-- Small steel tanks -->
  <svg class="banner banner--tanks" viewBox="0 0 1464 244" role="img" aria-label="Small Steel Tanks Fabrication banner">
    <rect class="fill-paper" width="1464" height="244"/>
    <polygon class="fill-blue" points="0,0 775,0 715,244 0,244"/>
    <polygon class="fill-blue" points="787,0 810,0 750,244 727,244"/>
    <polygon class="fill-grey" points="823,0 840,0 800,162 783,162"/>
    <polygon class="fill-grey" points="1170,0 1198,0 1144,164 1116,164"/>
    <polygon class="fill-grey" points="1212,0 1464,0 1464,244 1132,244"/>
    <text class="headline" x="42" y="102" font-size="64" textLength="650" lengthAdjust="spacingAndGlyphs">SMALL STEEL TANKS</text>
    <text class="headline" x="45" y="192" font-size="96" textLength="635" lengthAdjust="spacingAndGlyphs">FABRICATION</text>
    <text class="brand-name" x="972" y="140" font-size="50" text-anchor="middle">NORVALE</text>
    <g class="tagline tagline--light" font-size="36">
      <text x="1198" y="52">Show</text>
      <text x="1198" y="92">fabricated</text>
      <text x="1198" y="132">tanks and</text>
      <text x="1198" y="174">workshop</text>
      <text x="1198" y="214">craftsmanship</text>
    </g>
  </svg>

  <!-- General fabrication -->
  <svg class="banner banner--general" viewBox="0 0 1464 244" role="img" aria-label="General Fabrication Solutions banner">
    <rect class="fill-paper" width="1464" height="244"/>
    <polygon class="fill-blue" points="0,0 640,0 584,244 0,244"/>
    <polygon class="fill-blue" points="652,0 672,0 616,244 596,244"/>
    <polygon class="fill-grey" points="687,0 712,0 675,160 650,160"/>
    <polygon class="fill-grey" points="1090,0 1118,0 1063,164 1035,164"/>
    <polygon class="fill-grey" points="1132,0 1464,0 1464,244 1050,244"/>
    <text class="headline" x="55" y="80" font-size="78" textLength="333" lengthAdjust="spacingAndGlyphs">GENERAL</text>
    <text class="headline" x="55" y="143" font-size="78" textLength="515" lengthAdjust="spacingAndGlyphs">FABRICATION</text>
    <text class="headline" x="55" y="206" font-size="78" textLength="423" lengthAdjust="spacingAndGlyphs">SOLUTIONS</text>
    <text class="brand-name" x="850" y="140" font-size="50" text-anchor="middle">NORVALE</text>
    <g class="tagline tagline--light" font-size="36">
      <text x="1161" y="48">Broad steel</text>
      <text x="1161" y="88">fabrication</text>
      <text x="1161" y="128">theme for</text>
      <text x="1161" y="170">company-wide</text>
      <text x="1161" y="210">use</text>
    </g>
  </svg>

</main>
</body>
</html>
```